Yoga Training Cerificate

Design a certificate of graduation from a Vinyasa Yoga Teacher Training Program.

The attached document is an example of the certificate I received as a graduate from a teacher training program. You can use it as a template.

Stylistically, what you design can be: visually enticing, professional, clean, and modern.

Please develop the "Tidal Lotus" logo and embed it within the certificate.

Please add a circular watermark behind the body of the certificate similar to the one found in the attachment; leave out the words Asana Guild because I am not associated with that organization.

The name of my school is "Tidal Lotus." And it was established in 2017, which you can include.

The certificate affirms that "' 'such-and-such' has successfully completed the Tidal Lotus modern vinyasa yoga training, completing two hundred hours of instruction in practice and theory. Within the power of our institution as a certifying agent we declare Such-and-such, now, a teacher competent to share the gift of yoga with the masses in a safe and effective."

My name -Dennis Halvorsen- should be at bottom with a faux-signature; position title: Tidal Lotus founder.

If you decide to include text on the fringe, like the example, it might include bars of text describing the maxims of the Tidal Lotus school reading:

This is Tidal Lotus
Breath is primary
Evolve the physical culture
Bring your unique expression to the practice
Take Breaks
Freestyle
Close your eyes
Feel deeper into your body
This is active meditation
This is moving meditation
This is modern meditation

And find a way to integrate Emojis like: Fire, Water, Prayer Hands, etc. as you see fit.

Generally, make the certificate look: official, clear and clean. You can base it from the example given. And try and create a graphic design that is more visually capturing then the example.

```html
<!DOCTYPE html>
<html lang="en">
<head>
<meta charset="utf-8">
<title>Tidal Lotus Certificate of Completion</title>
<link rel="stylesheet" href="https://fonts.googleapis.com/css2?family=Libre+Baskerville:ital,wght@0,400;0,700;1,400&family=Yellowtail&display=swap">
<style>
  :root {
    --lavender: #cdbbf9;
    --band: #e17ae9;
    --bloom-soft: rgba(229, 128, 226, 0.45);
    --ring: rgba(232, 120, 220, 0.55);
    --star: rgba(232, 130, 226, 0.42);
    --ink: #1c1620;
    --paper-white: #ffffff;
  }
  * { margin: 0; padding: 0; box-sizing: border-box; }
  html, body { width: 1200px; height: 927px; overflow: hidden; background: var(--lavender); }
  .certificate {
    position: relative;
    width: 1200px;
    height: 927px;
    background: var(--lavender);
    overflow: hidden;
    font-family: "Libre Baskerville", Baskerville, Georgia, serif;
    color: var(--ink);
  }
  .backdrop { position: absolute; inset: 0; }

  .brand {
    position: absolute;
    top: 22px;
    left: 0;
    width: 1200px;
    text-align: center;
    font-weight: 700;
    font-size: 62px;
    line-height: 80px;
    color: var(--paper-white);
    white-space: nowrap;
  }
  .established {
    position: absolute;
    top: 90px;
    left: 790px;
    font-size: 13px;
    font-style: italic;
    color: var(--paper-white);
    white-space: nowrap;
  }

  .title-band {
    position: absolute;
    top: 132px;
    left: 0;
    width: 1200px;
    height: 126px;
    background: var(--band);
    display: flex;
    align-items: center;
    justify-content: center;
    gap: 14px;
    padding: 0 30px;
  }
  .title-rule {
    flex: 1 1 0;
    min-width: 40px;
    height: 3px;
    background: var(--paper-white);
  }
  .title {
    flex: 0 0 auto;
    font-family: "Yellowtail", "Brush Script MT", cursive;
    font-weight: 400;
    font-size: 92px;
    line-height: 126px;
    color: var(--paper-white);
    white-space: nowrap;
  }

  .body-copy {
    position: absolute;
    top: 508px;
    left: 209px;
    width: 880px;
    font-size: 18px;
    line-height: 27.5px;
  }
  .name-line {
    width: 326px;
    margin-left: 273px;
    border-top: 1.5px solid var(--ink);
    margin-bottom: 4px;
  }
  .name-line.declared { margin-top: 28px; }
  .statement span { display: block; white-space: nowrap; }

  .signature {
    position: absolute;
    left: 900px;
    top: 830px;
    width: 216px;
    text-align: center;
    border-top: 1.5px solid var(--ink);
    padding-top: 4px;
    font-size: 18px;
    line-height: 24px;
    white-space: nowrap;
  }
  .signature .signer { font-style: italic; }
</style>
</head>
<body>
<main class="certificate">
  <svg class="backdrop" width="1200" height="927" viewBox="0 0 1200 927" aria-hidden="true">
    <circle cx="45" cy="30" r="83" fill="var(--bloom-soft)"/>
    <circle cx="1091" cy="61" r="53" fill="var(--bloom-soft)"/>
    <circle cx="1139" cy="68" r="45" fill="var(--bloom-soft)"/>
    <circle cx="1182" cy="68" r="23" fill="var(--bloom-soft)"/>
    <circle cx="98" cy="826" r="100" fill="var(--bloom-soft)"/>
    <circle cx="129" cy="811" r="68" fill="var(--bloom-soft)"/>
    <circle cx="1045" cy="890" r="178" fill="var(--bloom-soft)"/>
    <circle cx="600" cy="568" r="437" fill="none" stroke="var(--ring)" stroke-width="6"/>
    <polygon fill="var(--star)"
      points="600,60 699,364 1018,364 760,552 859,856 600,668 341,856 440,552 182,364 501,364"/>
  </svg>

  <div class="brand">TIDAL LOTUS</div>
  <div class="established">establish 2017</div>

  <header class="title-band">
    <span class="title-rule"></span>
    <h1 class="title">Certificate of Completion</h1>
    <span class="title-rule"></span>
  </header>

  <section class="body-copy">
    <div class="name-line graduate"></div>
    <p class="statement opening">
      <span>has successfully completed the Tidal Lotus modern vinyasa yoga training, completing</span>
      <span>two-hundred hours of instruction in practice and theory. Within the power of our</span>
      <span>institution as a certifying agent we declare:</span>
    </p>
    <div class="name-line declared"></div>
    <p class="statement closing">
      <span>now, a teacher competent to share the gift of yoga with the masses in a safe and effective.</span>
    </p>
  </section>

  <div class="signature">
    <div class="signer">-Dennis Halvorsen-</div>
    <div class="role">Tidal Lotus founder.</div>
  </div>
</main>
</body>
</html>
```